US company marketing to law enforcement needs brochure design

We have created a new logo and now need to update our printed material. What we really need is a "style" or "template" for how our brochures will look in the future. Enclosed is the brochure draft with the old style and logo. Also enclosed is the new logo. As we are marketing to US law enforcement it is important the the brochure design is strong, powerful and that we are looking experienced and trustworthy. However, we also want to look modern in line with the logo update.

Target Market(s)

Law enforcement

Industry/Entity Type

Marketing

```html
<!DOCTYPE html>
<html lang="en">
<head>
<meta charset="utf-8">
<title>Steadfast Programs – Brochure</title>
<link rel="stylesheet" href="https://fonts.googleapis.com/css2?family=Open+Sans:wght@300;400;600;700&display=swap">
<style>
  :root {
    --navy: #2c3f6d;
    --navy-deep: #233459;
    --navy-light: #3b5593;
    --blue: #3d5b9c;
    --blue-tab: #34508c;
    --blue-active: #5479c2;
    --ink: #3b3f4a;
    --muted: #6b7386;
    --paper: #ffffff;
    --paper-shade: #eef0f4;
    --stage: #e6e7ea;
  }
  * { box-sizing: border-box; margin: 0; padding: 0; }
  html, body { width: 1200px; height: 804px; overflow: hidden; }
  body {
    background: var(--stage);
    font-family: "Open Sans", Arial, sans-serif;
    color: var(--ink);
    position: relative;
  }

  /* ---------- Cover ---------- */
  .cover {
    position: absolute; left: 70px; top: 162px;
    width: 340px; height: 480px;
    background: var(--paper);
    box-shadow: 0 4px 14px rgba(0,0,0,.18);
    overflow: hidden;
  }
  .cover-photo {
    height: 195px;
    background: linear-gradient(160deg, #1c1f26 0%, #3a3d44 40%, #c9a676 75%, #e8e4dc 100%);
  }
  .cover-brand {
    height: 60px;
    display: flex; align-items: center; justify-content: center; gap: 8px;
    background: linear-gradient(#ffffff, #eef0f4);
  }
  .brand-dot { width: 18px; height: 18px; border-radius: 50%; background: var(--navy); }
  .brand-name { font-size: 15px; font-weight: 300; color: #5a6682; letter-spacing: .1px; }
  .cover-panel {
    position: absolute; left: 0; right: 0; top: 255px; bottom: 0;
    background: linear-gradient(180deg, var(--navy-deep) 0%, var(--navy) 45%, var(--navy-light) 100%);
  }
  .cover-tagline {
    margin-top: 14px; text-align: center;
    font-size: 6.5px; font-style: italic; color: #d7def0;
  }
  .cover-programs {
    position: absolute; left: 14px; right: 14px; bottom: 16px;
    display: flex; justify-content: space-between;
    font-size: 4.6px; font-weight: 700; letter-spacing: .3px;
    text-transform: uppercase; color: #7e97cf;
  }

  /* ---------- Spread ---------- */
  .spread {
    position: absolute; left: 430px; top: 162px;
    width: 680px; height: 480px;
    display: flex;
    box-shadow: 0 4px 14px rgba(0,0,0,.18);
  }
  .page {
    position: relative; width: 340px; height: 480px;
    background: var(--paper); overflow: hidden;
  }
  .page-left { background: linear-gradient(90deg, #ffffff 85%, #e4e6ec 100%); }
  .page-right { background: linear-gradient(90deg, #e4e6ec 0%, #ffffff 12%); }

  .spread-title {
    position: absolute; left: 28px; top: 36px;
    font-size: 21px; font-weight: 300; line-height: 1.15; color: var(--blue);
  }
  .program-tabs {
    position: absolute; left: 0; right: 0; top: 104px; height: 22px;
    display: flex; background: var(--blue-tab);
  }
  .program-tabs span {
    flex: auto; display: flex; align-items: center; justify-content: center;
    font-size: 5.2px; font-weight: 700; letter-spacing: .3px;
    text-transform: uppercase; color: #dfe6f6;
    border-right: 1px solid rgba(255,255,255,.2);
  }
  .program-tabs .is-active { background: var(--blue-active); color: #fff; border-right: 0; }

  .section-title {
    font-size: 9px; font-weight: 600; color: var(--blue); margin-bottom: 6px;
  }
  .body-copy {
    font-size: 5.6px; line-height: 1.75; color: var(--ink);
  }
  .professionals { position: absolute; left: 28px; top: 150px; width: 140px; }
  .staff-photo {
    position: absolute; left: 182px; top: 150px; width: 128px; height: 168px;
    background: linear-gradient(180deg, #7f91c2 0%, #4f63a0 55%, #3b4d86 100%);
  }
  .feature-photo {
    position: absolute; left: 20px; top: 330px; width: 292px; height: 128px;
    background: linear-gradient(180deg, #ffffff 0%, #f1ece4 45%, #d8d2c8 80%, #5a3a2c 100%);
  }

  .benefits { position: absolute; left: 26px; top: 36px; width: 172px; }
  .benefit { margin-bottom: 26px; }
  .benefit:nth-child(2) { margin-top: 18px; }
  .benefit:nth-child(3) { margin-top: 30px; }

  .services { position: absolute; left: 212px; top: 36px; width: 112px; }
  .service { margin-bottom: 22px; }
  .service-label {
    display: flex; align-items: center; gap: 5px; margin-bottom: 6px;
    font-size: 5px; font-weight: 600; color: var(--navy);
  }
  .service-label i { width: 11px; height: 11px; border-radius: 50%; background: var(--navy); flex: none; }
  .service-box {
    background: linear-gradient(160deg, var(--navy-deep), var(--navy-light));
    padding: 10px 0 10px 22px;
    list-style: none;
  }
  .service-box li {
    font-size: 5.4px; font-weight: 700; color: #fff; line-height: 2;
  }
  .closing-note {
    position: absolute; right: 22px; top: 432px; width: 150px;
    text-align: right; font-size: 5.4px; font-weight: 700; line-height: 1.7; color: var(--blue);
  }
</style>
</head>
<body>

<section class="cover">
  <div class="cover-photo" role="img" aria-label="Photo of a judge signing papers at a desk beside a wooden gavel"></div>
  <div class="cover-brand">
    <span class="brand-dot"></span>
    <span class="brand-name">Steadfast Programs</span>
  </div>
  <div class="cover-panel">
    <p class="cover-tagline">A Dependable Partner for Court-Ordered Program Management</p>
    <div class="cover-programs">
      <span>Pre-Trial</span><span>Diversion</span><span>Deferred Prosecution</span><span>Jail Alternative</span><span>Probation</span>
    </div>
  </div>
</section>

<section class="spread">
  <article class="page page-left">
    <h1 class="spread-title">Solutions for<br>your jurisdiction's needs</h1>
    <nav class="program-tabs">
      <span>Pre-Trial</span><span>Diversion</span><span>Deferred Prosecution</span><span>Jail Alternative</span><span class="is-active">Probation</span>
    </nav>
    <div class="professionals">
      <h2 class="section-title">Experienced Professionals</h2>
      <p class="body-copy">Our field staff bring years of court and supervision experience to every program. Each officer is trained to manage intake, testing, reporting and case review with care. Agencies gain a steady partner that keeps records current, answers questions quickly and helps every participant stay on track from the first meeting to the final report.</p>
    </div>
    <div class="staff-photo" role="img" aria-label="Blue-toned photo of a staff member working at an office desk"></div>
    <div class="feature-photo" role="img" aria-label="Photo of a wooden gavel resting on an open law book"></div>
  </article>

  <article class="page page-right">
    <div class="benefits">
      <div class="benefit">
        <h2 class="section-title">Control Transparency</h2>
        <p class="body-copy">Courts see every payment, test result and check-in as it happens. Clear monthly summaries show progress by case, and secure online access lets judges and staff review files at any time without extra paperwork or phone calls.</p>
      </div>
      <div class="benefit">
        <h2 class="section-title">Save / Reduce Case Loads</h2>
        <p class="body-copy">We handle daily supervision tasks so probation officers can focus on higher risk cases. Intake, scheduling, reminders and compliance tracking are managed by our team, reducing workload while keeping the court fully informed of every outcome.</p>
      </div>
      <div class="benefit">
        <h2 class="section-title">Technology / Equipment</h2>
        <p class="body-copy">Modern testing equipment, GPS monitoring and a secure case system give agencies dependable tools. Every device is maintained by our staff, and results are logged within hours so the right people always have the latest information.</p>
      </div>
    </div>

    <div class="services">
      <div class="service">
        <div class="service-label"><i></i>Custom Solution</div>
        <ul class="service-box"><li>Lorem Ipsum</li><li>Lorem Ipsum</li><li>Lorem Ipsum</li><li>Lorem Ipsum</li><li>Lorem Ipsum</li></ul>
      </div>
      <div class="service">
        <div class="service-label"><i></i>Full Menu</div>
        <ul class="service-box"><li>Lorem Ipsum</li><li>Lorem Ipsum</li><li>Lorem Ipsum</li><li>Lorem Ipsum</li></ul>
      </div>
      <div class="service">
        <div class="service-label"><i></i>Comprehensive<br>Administrative Services</div>
        <ul class="service-box"><li>Lorem Ipsum</li><li>Lorem Ipsum</li><li>Lorem Ipsum</li><li>Lorem Ipsum</li></ul>
      </div>
    </div>

    <p class="closing-note">Morbi auctor ligula tellus. Duis pellentesque, ligula id luctus aliquet, magna ante mattis tortor.</p>
  </article>
</section>

</body>
</html>
```